Remedial massage therapist or clinical look

I would like a plain white or light colour background with front view of a musculoskeletal human body on the from on the left hand side, with Mira Dostane remedial and sports massage therapist. On the back I want the back view of the musculoskeletal body on the left side with Mira Dostane remedial and sports massage therapist, my contact details and appointment time and date. The colour of writing can be the same or close colour to the musculoskeletal body.
I don't want it to look to busy but also don't want it to be to plain,

Industry/Entity Type

Massage

Contact Information for Business Card

Mira Dostane
Remedial and Sports Massage Therapist
Contact number: 0481536207
Email: dostanemira41@quillmark.net

```html
<!DOCTYPE html>
<html lang="en">
<head>
<meta charset="utf-8">
<title>Mira Dostane – Remedial and Sports Massage Therapist</title>
<link rel="stylesheet" href="https://fonts.googleapis.com/css2?family=Noto+Serif&family=Tinos&display=swap">
<style>
  :root {
    --paper: #fdfcf9;
    --ribbon: #ece6d9;
    --ribbon-soft: rgba(236,230,217,0.45);
    --ink: #de40f2;
    --figure-deep: #e055f5;
    --figure-mid: #e672f7;
    --figure-light: #f0a6f9;
    --dots: #9a9a9a;
  }
  * { margin: 0; padding: 0; box-sizing: border-box; }
  html, body { width: 694px; height: 1200px; overflow: hidden; background: var(--paper); }
  .card {
    position: relative;
    width: 694px;
    height: 1200px;
    background: var(--paper);
    overflow: hidden;
    font-family: "Noto Serif", serif;
    color: var(--ink);
  }
  .ribbons {
    position: absolute;
    left: 50px; top: 0;
    width: 400px; height: 1200px;
    background:
      radial-gradient(ellipse 60% 22% at 40% 8%, var(--ribbon) 0%, rgba(236,230,217,0) 100%),
      radial-gradient(ellipse 55% 25% at 65% 48%, var(--ribbon) 0%, rgba(236,230,217,0) 100%),
      radial-gradient(ellipse 60% 24% at 35% 82%, var(--ribbon) 0%, rgba(236,230,217,0) 100%),
      linear-gradient(90deg, rgba(253,252,249,0) 0%, var(--ribbon-soft) 25%, var(--ribbon-soft) 70%, rgba(253,252,249,0) 100%);
  }
  .anatomy-figure {
    position: absolute;
    left: 64px; top: 60px;
    width: 194px; height: 1050px;
    border-radius: 97px 6px 30px 60px / 120px 6px 40px 80px;
    background:
      radial-gradient(ellipse 70% 12% at 60% 4%, var(--figure-deep) 0%, rgba(224,85,245,0) 100%),
      radial-gradient(ellipse 50% 30% at 50% 35%, var(--figure-mid) 0%, rgba(230,114,247,0) 100%),
      linear-gradient(180deg, var(--figure-deep) 0%, var(--figure-mid) 30%, var(--figure-light) 55%, var(--figure-mid) 80%, var(--figure-deep) 100%);
    opacity: 0.92;
  }
  .rules { position: absolute; left: 0; top: 0; }
  .text { position: absolute; left: 324px; white-space: nowrap; font-weight: 400; }
  .name { top: 50px; font-size: 74px; line-height: 86px; letter-spacing: 1px; }
  .role { top: 258px; font-size: 40px; line-height: 46px; letter-spacing: 1.5px; }
  .phone { top: 448px; font-size: 48px; line-height: 56px; letter-spacing: 2px; }
  .email { top: 546px; left: 318px; font-family: "Tinos", serif; font-size: 26px; line-height: 30px; letter-spacing: 0.4px; }
  .appointment { top: 618px; font-size: 41px; line-height: 46px; letter-spacing: 1px; }
</style>
</head>
<body>
  <div class="card">
    <div class="ribbons" role="img" aria-label="Soft flowing beige ribbon background"></div>
    <div class="anatomy-figure" role="img" aria-label="Back view illustration of a musculoskeletal human body in magenta"></div>

    <svg class="rules" width="694" height="1200" viewBox="0 0 694 1200" aria-hidden="true">
      <g stroke="var(--dots)" stroke-width="4" stroke-linecap="round" stroke-dasharray="0 10.5" fill="none">
        <line x1="274" y1="62" x2="274" y2="1102"/>
        <line x1="284" y1="240" x2="664" y2="240"/>
        <line x1="284" y1="418" x2="664" y2="418"/>
        <line x1="284" y1="523" x2="664" y2="523"/>
        <line x1="284" y1="596" x2="664" y2="596"/>
      </g>
    </svg>

    <h1 class="text name">Mira<br>Dostane</h1>
    <p class="text role">Remedial and<br>Sports Massage<br>Therapist</p>
    <p class="text phone">048 153 6207</p>
    <p class="text email">dostanemira41@quillmark.net</p>
    <p class="text appointment">Appointment<br>time and date:</p>
  </div>
</body>
</html>
```